QUELTRAN POWERLINE SERVICES needs a vibrant design for electrical contracting work.

I require a card design for my own electrical contracting business. I will be doing a lot of domestic and commercial work, including things such as repairs, maintenance, lighting, installations and various others. LED lighting and energy efficiency will be a big part of my business. I wish not to have childish pictures such as light bulbs in the design, but rather a smart and modern looking card which incorporates my logo colours and perhaps the same lighting strike within the faded background of the card.

Target Market(s)

Residential and Commercial property owners.

Industry/Entity Type

Electrical

Contact Information for Business Card

Dalen Voskic
EC40923
Phone Number: 0417 358 942
Email: dalen@queltranpower.com

Font styles to use
Serif
Sans Serif

Requirements
Must have
• My Logo and associated colours.
Nice to have
• Some form of shapes splitting the card into different colours related to the colours of my logo. Electric Blue, Silver/Grey and White.
Should not have
• Childish pictures and symbols such as light bulbs.

```html
<!DOCTYPE html>
<html lang="en">
<head>
<meta charset="utf-8">
<title>Queltran Powerline Services – Business Card</title>
<link rel="stylesheet" href="https://fonts.googleapis.com/css2?family=Arimo:wght@400;700&display=swap">
<style>
  :root {
    --page: #ffffff;
    --silver: #d1d2d4;
    --steel-light: #828386;
    --steel: #6b6c70;
    --electric-blue: #3a53a4;
    --blue-shade: #2c4279;
    --navy: #0b2a58;
    --name-navy: #15315f;
    --white: #ffffff;
    --card-edge: #333333;
  }
  html, body {
    margin: 0;
    padding: 0;
    width: 1200px;
    height: 927px;
    overflow: hidden;
    background: var(--page);
    font-family: "Arimo", Arial, sans-serif;
  }
  .canvas {
    position: relative;
    width: 1200px;
    height: 927px;
  }
  .business-card {
    position: absolute;
    left: 108px;
    top: 133px;
    width: 860px;
    height: 491px;
    outline: 1px solid var(--card-edge);
    overflow: hidden;
    background: var(--silver);
  }
  .card-shapes {
    position: absolute;
    inset: 0;
    width: 860px;
    height: 491px;
  }
  .shape-steel-light { fill: var(--steel-light); }
  .shape-steel { fill: var(--steel); }
  .shape-blue { fill: var(--electric-blue); }
  .shape-blue-shade { fill: var(--blue-shade); }
  .shape-navy { fill: var(--navy); }

  .brand {
    position: absolute;
    left: 30px;
    top: 26px;
    display: flex;
    align-items: center;
    gap: 12px;
  }
  .brand-dot {
    width: 76px;
    height: 76px;
    border-radius: 50%;
    background: var(--steel-light);
  }
  .brand-name {
    color: var(--electric-blue);
    font-weight: 700;
    line-height: 1;
  }
  .brand-name .line-main {
    display: block;
    font-size: 54px;
    letter-spacing: 1px;
  }
  .brand-name .line-sub {
    display: block;
    font-size: 21px;
    letter-spacing: 1.2px;
    margin-top: 6px;
  }

  .contact {
    position: absolute;
    left: 438px;
    top: 262px;
    color: var(--white);
  }
  .contact-name {
    margin: 0;
    font-size: 32px;
    font-weight: 700;
    color: var(--name-navy);
    letter-spacing: 1px;
    line-height: 1;
  }
  .licence {
    margin: 3px 0 0 68px;
    font-size: 22px;
    line-height: 1.1;
  }
  .contact-row {
    display: flex;
    align-items: center;
    gap: 6px;
    margin: 0;
    line-height: 1;
  }
  .contact-row.phone { font-size: 33px; margin-top: 9px; }
  .contact-row.email { font-size: 29px; margin-top: 10px; }
  .contact-icon {
    width: 26px;
    height: 26px;
    flex: none;
  }
</style>
</head>
<body>
<div class="canvas">
  <div class="business-card">
    <svg class="card-shapes" viewBox="0 0 860 491" aria-hidden="true">
      <polygon class="shape-steel-light" points="0,491 567,0 620,0"/>
      <polygon class="shape-steel" points="0,491 620,0 860,0"/>
      <polygon class="shape-blue" points="0,491 860,0 860,491"/>
      <polygon class="shape-blue-shade" points="0,491 860,404 382,491"/>
      <polygon class="shape-navy" points="382,491 860,404 860,491"/>
    </svg>

    <div class="brand">
      <div class="brand-dot"></div>
      <div class="brand-name">
        <span class="line-main">QUELTRAN</span>
        <span class="line-sub">POWERLINE SERVICES</span>
      </div>
    </div>

    <div class="contact">
      <h1 class="contact-name">Dalen Voskic</h1>
      <p class="licence">EC40923</p>
      <p class="contact-row phone">
        <svg class="contact-icon" viewBox="0 0 26 26" aria-hidden="true">
          <circle cx="13" cy="13" r="13" fill="#fff"/>
          <path d="M8.5 6.5c.6-.5 1.4-.4 1.8.2l1.4 2.2c.3.5.2 1.2-.2 1.6l-.9.8c.7 1.6 2 3 3.6 3.8l.8-.9c.4-.4 1.1-.5 1.6-.2l2.2 1.4c.6.4.7 1.2.2 1.8l-1 1.1c-.7.7-1.8 1-2.8.6-3.8-1.4-6.6-4.3-8-8-.4-1 0-2.1.7-2.8z" fill="#3a53a4"/>
        </svg>
        0417 358 942
      </p>
      <p class="contact-row email">
        <svg class="contact-icon" viewBox="0 0 26 26" aria-hidden="true">
          <circle cx="13" cy="13" r="13" fill="#fff"/>
          <rect x="6.5" y="8.5" width="13" height="9" rx="1" fill="#3a53a4"/>
          <path d="M6.8 9l6.2 4.6L19.2 9" fill="none" stroke="#fff" stroke-width="1.3"/>
        </svg>
        dalen@queltranpower.com
      </p>
    </div>
  </div>
</div>
</body>
</html>
```